OurPlume Lifting Hope across a trusted circle

I am looking for a sleek, clean and simple app design. I need also a payment page and offering different packages and payment types.

I would like the color scheme to be black or white very futuristic like the movie q-lantern.

The profile page displaying the picture, as clean and future like as possible.

Share profile options, manage subscription, update profile, help ect….

On the verified page last one, the social media logos are interactive so the user can share their info through the connected social media account.

Target Market(s)

Professionals and individuals.

Industry/Entity Type

Due diligence & background checks verification

Font styles to use
Sans Serif

Colors
0054AA
0677BA
7BADD7
CADEEF
E8F1F8
0094D4
00A9DD
6FCCEA
C7EBF8
E9F6FB
59FF00
82FF00
B8FF75
E3FFCB
F4FFEA

Requirements
Must have
• The ability to add my social media links or log in through the app directly for direct confirmation. After email entered on account sign up they get either a confirmation email or a text through telephone number verification.
Nice to have
• Account creation to add profile picture must take a selfie.

```html
<!DOCTYPE html>
<html lang="en">
<head>
<meta charset="utf-8">
<title>OurPlume – Login, Dashboard and Profile</title>
<link href="https://fonts.googleapis.com/css2?family=Lato:wght@400;700;900&display=swap" rel="stylesheet">
<style>
:root{
  --bg:#262a31;
  --phone:#2b2f36;
  --phone-dark:#24272d;
  --field:#23262c;
  --cyan:#0ae3ee;
  --cyan-deep:#00b8cc;
  --white:#f4f6f8;
  --muted:#9aa0a8;
  --dim:#7d838c;
  --photo-light:#eab583;
  --photo-dark:#d99a63;
  --shadow-dark:rgba(10,12,15,.55);
  --shadow-light:rgba(70,76,86,.35);
}
*{box-sizing:border-box;margin:0;padding:0}
html,body{width:1200px;height:804px;overflow:hidden}
body{background:var(--bg);font-family:"Lato",sans-serif;color:var(--white);position:relative}
.phone{position:absolute;width:255px;height:554px;background:var(--phone);border-radius:26px;
  box-shadow:14px 18px 36px var(--shadow-dark),-6px -6px 16px var(--shadow-light);overflow:hidden}
.abs{position:absolute}
.center{left:0;right:0;text-align:center}
.round-btn{position:absolute;border-radius:50%;background:var(--phone);
  box-shadow:4px 4px 9px var(--shadow-dark),-3px -3px 7px var(--shadow-light);
  display:flex;align-items:center;justify-content:center}
.photo{position:absolute;border-radius:10px;border:1.5px solid var(--cyan);
  background:radial-gradient(circle at 50% 40%,var(--photo-light),var(--photo-dark));
  box-shadow:6px 10px 16px var(--shadow-dark)}
.sheet{position:absolute;left:0;right:0;bottom:0;background:var(--phone-dark);border-radius:24px 24px 0 0;
  box-shadow:0 -6px 14px rgba(10,12,15,.35)}
.sheet .handle{position:absolute;top:7px;left:50%;width:32px;height:2px;margin-left:-16px;background:#15171b;border-radius:2px}
.cyan-btn{position:absolute;border-radius:50%;background:radial-gradient(circle at 40% 35%,#3ff2f7,var(--cyan-deep));
  box-shadow:0 0 22px rgba(10,227,238,.45),4px 6px 10px var(--shadow-dark);display:flex;align-items:center;justify-content:center;color:#fff}

/* login */
.login{left:136px;top:95px}
.brand{top:56px;font-size:13px;color:var(--cyan)}
.login-title{top:70px;font-size:26px;font-weight:900;letter-spacing:.5px}
.field{position:absolute;left:35px;width:192px;height:31px;border-radius:16px;background:var(--field);
  box-shadow:inset 3px 3px 6px rgba(8,10,12,.6),0 0 10px rgba(10,227,238,.12);
  display:flex;align-items:center;padding-left:14px;gap:8px;font-size:9px;color:var(--muted)}
.forgot{right:28px;top:266px;font-size:9px;color:var(--muted)}
.login-btn{left:94px;top:313px;width:66px;height:66px;font-size:11px;font-weight:700}
.login .sheet{height:126px}
.sheet-title{font-size:12px;font-weight:900}
.sheet-sub{font-size:8.5px;color:var(--muted)}

/* dashboard */
.dash{left:473px;top:49px}
.user-name{top:21px;font-size:9.5px;font-weight:900}
.user-role{top:34px;font-size:9px;color:var(--muted)}
.section{left:23px;font-size:12px;font-weight:900}
.stat{position:absolute;top:257px;font-size:9px;color:var(--muted)}
.stat b{display:block;margin-top:6px;color:var(--white);font-weight:900}
.card{position:absolute;top:341px;width:77px;height:80px;border-radius:8px;background:var(--phone-dark);
  box-shadow:3px 4px 8px var(--shadow-dark);padding:10px 8px}
.card .mark{width:20px;height:20px;border-radius:50%;border:2px solid var(--dim)}
.card .mark.on{border-color:var(--cyan);background:rgba(10,227,238,.15)}
.card .name{position:absolute;top:49px;left:8px;font-size:9px;font-weight:900}
.card .state{position:absolute;top:62px;left:8px;font-size:9px;color:var(--muted)}
.dash .sheet{height:74px}

/* profile */
.profile{left:809px;top:187px}
.page-title{top:30px;font-size:12px;font-weight:900}
.verified{left:93px;top:192px;width:80px;height:15px;border-radius:8px;background:var(--cyan);
  font-size:6.5px;color:#0b3c44;display:flex;align-items:center;justify-content:center;gap:3px}
.info{position:absolute;font-size:7px;color:var(--dim)}
.info span{display:block;margin-top:4px;font-size:9.5px;color:#c7ccd2}
.share{left:24px;top:408px;width:209px;height:37px;border-radius:19px;background:var(--phone);
  box-shadow:4px 5px 10px var(--shadow-dark),-3px -3px 7px var(--shadow-light);
  font-size:9.5px;color:#c7ccd2;display:flex;align-items:center;justify-content:center}
.or{top:466px;font-size:7px;color:var(--muted)}
.net{top:490px;width:37px;height:37px;font-size:6px;font-weight:700;color:#c7ccd2}
</style>
</head>
<body>

<section class="phone login">
  <div class="abs center brand">OurPlume</div>
  <h1 class="abs center login-title">LOGIN</h1>
  <div class="field" style="top:158px">
    <svg width="12" height="10" viewBox="0 0 12 10" fill="none" stroke="var(--cyan)" stroke-width="1.2"><rect x=".6" y=".6" width="10.8" height="8.8" rx="1.5"/><path d="M1 1.5l5 4 5-4"/></svg>
    Email
  </div>
  <div class="field" style="top:216px">
    <svg width="10" height="12" viewBox="0 0 10 12" fill="none" stroke="var(--cyan)" stroke-width="1.2"><rect x="1" y="5" width="8" height="6.4" rx="2"/><path d="M3 5V3.5a2 2 0 0 1 4 0"/><circle cx="5" cy="8" r=".8"/></svg>
    Password
  </div>
  <div class="abs forgot">Forgot password?</div>
  <div class="cyan-btn login-btn">Login</div>
  <div class="sheet">
    <div class="handle"></div>
    <div class="abs sheet-title" style="left:21px;top:28px">Don’t have Account?</div>
    <div class="abs sheet-sub" style="left:21px;top:47px">Create now</div>
    <div class="round-btn" style="left:190px;top:23px;width:39px;height:39px;background:var(--phone-dark)">
      <svg width="13" height="13" viewBox="0 0 13 13" stroke="var(--muted)" stroke-width="1.2"><path d="M6.5 0v13M0 6.5h13"/></svg>
    </div>
  </div>
</section>

<section class="phone dash">
  <div class="round-btn" style="left:21px;top:21px;width:30px;height:30px">
    <svg width="9" height="6" viewBox="0 0 9 6" stroke="var(--muted)" stroke-width="1.2"><path d="M0 1h9M0 5h6"/></svg>
  </div>
  <div class="abs center user-name">Dorian Vasquez</div>
  <div class="abs center user-role">Engineer</div>
  <div class="round-btn" style="left:203px;top:21px;width:30px;height:30px">
    <svg width="9" height="10" viewBox="0 0 9 10" fill="none" stroke="var(--muted)" stroke-width="1.1"><circle cx="4.5" cy="3" r="2.3"/><path d="M.7 9.5a3.8 3.8 0 0 1 7.6 0z"/></svg>
  </div>
  <div class="photo" style="left:37px;top:73px;width:181px;height:124px" role="img" aria-label="Portrait photo of the member"></div>
  <h2 class="abs section" style="top:228px">My Followers</h2>
  <div class="stat" style="left:29px">Linkhall<b>116k</b></div>
  <div class="stat" style="left:90px">Chirrup<b>145k</b></div>
  <div class="stat" style="left:141px">Snapframe<b>—</b></div>
  <div class="stat" style="left:200px">Workweb<b>157k</b></div>
  <h2 class="abs section" style="top:312px">My Social medias</h2>
  <div class="card" style="left:23px"><div class="mark"></div><div class="name">Snapframe</div><div class="state">Not completed</div></div>
  <div class="card" style="left:116px"><div class="mark on"></div><div class="name">Linkhall</div><div class="state">Completed</div></div>
  <div class="card" style="left:210px"><div class="mark on"></div><div class="name">Chirrup</div><div class="state">Completed</div></div>
  <div class="sheet">
    <div class="handle" style="top:9px"></div>
    <div class="abs sheet-title" style="left:21px;top:26px">Complete Profile</div>
    <div class="abs sheet-sub" style="left:21px;top:46px;font-size:8px">Snapframe not connected. Connect now</div>
    <div class="cyan-btn" style="left:193px;top:17px;width:40px;height:40px">
      <svg width="6" height="10" viewBox="0 0 6 10" fill="none" stroke="#fff" stroke-width="1.6"><path d="M1 1l4 4-4 4"/></svg>
    </div>
  </div>
</section>

<section class="phone profile">
  <div class="round-btn" style="left:22px;top:22px;width:30px;height:30px">
    <svg width="9" height="8" viewBox="0 0 9 8" fill="none" stroke="var(--muted)" stroke-width="1.2"><path d="M9 4H1M4 1L1 4l3 3"/></svg>
  </div>
  <h1 class="abs center page-title">Profile</h1>
  <div class="round-btn" style="left:204px;top:22px;width:30px;height:30px">
    <svg width="10" height="10" viewBox="0 0 10 10" fill="none" stroke="var(--muted)" stroke-width="1"><path d="M4 1H1v8h8V6"/><path d="M8 .8l1.2 1.2L5 6.2 3.6 6.4 3.8 5z"/></svg>
  </div>
  <div class="photo" style="left:38px;top:74px;width:181px;height:125px" role="img" aria-label="Portrait photo of the verified member"></div>
  <div class="abs verified">
    <svg width="7" height="7" viewBox="0 0 7 7"><circle cx="3.5" cy="3.5" r="3.5" fill="#0b3c44"/><path d="M2 3.6l1 1 2-2" stroke="var(--cyan)" stroke-width=".9" fill="none"/></svg>
    OurPlume verified
  </div>
  <div class="info" style="left:26px;top:251px">Full Name<span>Dorian Vasquez</span></div>
  <div class="info" style="left:154px;top:251px">Birthday<span>15 March 1990</span></div>
  <div class="info" style="left:26px;top:303px">Email ID<span>d.vasquez@plumemail.com</span></div>
  <div class="info" style="left:154px;top:303px">Phone Number<span>555 0192 347</span></div>
  <div class="info" style="left:26px;top:354px">Location<span>New York</span></div>
  <div class="info" style="left:154px;top:354px">Employment Match<span>15 March 1990</span></div>
  <div class="abs share">Share Profile</div>
  <div class="abs center or">OR</div>
  <div class="round-btn net" style="left:22px">Linkhall</div>
  <div class="round-btn net" style="left:79px">Snapframe</div>
  <div class="round-btn net" style="left:137px">Workweb</div>
  <div class="round-btn net" style="left:194px">Chirrup</div>
</section>

</body>
</html>
```